Harborline Hound Fair Website Bright, colorful, hip

Expo website.
Harborline Hound Fair May 11th, 2019 from 11am-6pm
Wexley Green, Baltimore MD
220 Exhibitors from NY to D.C.! Talks on BSL and Animal cruelty! Food Trucks! Live Music! On-Site Adoptions with T.O.P.S.s, Renowned Pitbull advocates Velvet Paws Collective and Kindness Knows No Breed, Baltimore rescue Harbor Lantern Rescue! Games! Contest! Kids Corner!

Target Market(s)

Pet Owners

Industry/Entity Type

Event

Number of Pages Required

2 page

Font styles to use
Sans Serif

Colors

Designer to choose colors to be used in the design.

Requirements
Must have
• Branded header. Slider with "features". Blog page. Google Map of Wexley Green.
• "Want to be an exhibitor?!? Click here!"
Nice to have
• Bright and Bold. Super modern
Should not have
• White Space. Dont want to look like the other site I've done on this platform.

```html
<!DOCTYPE html>
<html lang="en">
<head>
<meta charset="utf-8">
<title>Harborline Hound Fair</title>
<link rel="stylesheet" href="https://fonts.googleapis.com/css2?family=Oswald:wght@300;400;500&family=Poppins:wght@400;500&display=swap">
<style>
:root{
  --yellow:#fdc10e;
  --yellow-deep:#f5b400;
  --red:#e4112b;
  --ink:#111111;
  --dark:#1d1b17;
  --white:#ffffff;
  --map:#e9e7e2;
  --park:#bfe0a8;
}
*{margin:0;padding:0;box-sizing:border-box}
html,body{width:1200px;height:2490px;overflow:hidden;background:var(--yellow)}
body{position:relative;font-family:'Poppins',sans-serif;color:var(--ink)}

.hero{position:absolute;left:0;top:0;width:1200px;height:728px;
  background:linear-gradient(180deg,#3c4a5c 0%,#2c3a33 35%,#26371e 62%,#3e5628 100%)}
.hero-emblem{position:absolute;left:500px;top:125px;width:200px;height:200px;border-radius:50%;
  background:var(--white);display:flex;align-items:center;justify-content:center;text-align:center;
  font-family:'Oswald',sans-serif;font-weight:500;font-size:24px;line-height:1.2;color:var(--ink);padding:30px}
.ribbon{position:absolute;left:260px;width:680px;height:68px}
.ribbon svg{position:absolute;inset:0}
.ribbon span{position:relative;display:block;text-align:center;line-height:68px;
  font-family:'Oswald',sans-serif;font-weight:400;font-size:37px}
.ribbon.name{top:346px}
.ribbon.date{top:428px}
.ribbon.date span{color:var(--white)}
.ribbon.venue{top:509px}

.happenings{position:absolute;left:0;top:655px;width:1200px;height:575px}
.happenings .edge{position:absolute;left:0;top:0}
.happenings h2{position:absolute;top:135px;width:100%;text-align:center;
  font-family:'Oswald',sans-serif;font-weight:400;font-size:42px}
.list{position:absolute;list-style:none;font-family:'Oswald',sans-serif;font-weight:300;font-size:20px;line-height:32px}
.list li{position:relative;padding-left:38px;margin-bottom:20px}
.list li svg{position:absolute;left:0;top:6px}
.list.left{left:116px;top:276px}
.list.right{left:788px;top:251px;width:320px}
.partner{position:absolute;left:415px;top:241px;width:350px;height:232px;display:flex;flex-direction:column;align-items:center;justify-content:center;gap:16px}
.partner .dot{width:70px;height:70px;border-radius:50%;background:var(--ink)}
.partner p{font-family:'Oswald',sans-serif;font-weight:500;font-size:34px;color:var(--ink);text-align:center;line-height:1.1}

.blog{position:absolute;left:0;top:1228px;width:1200px;height:640px;
  background:radial-gradient(ellipse at 50% 45%,#3a3126 0%,#1f1c17 60%,#141310 100%)}
.blog h2{position:absolute;top:75px;width:100%;text-align:center;color:var(--white);
  font-family:'Oswald',sans-serif;font-weight:400;font-size:42px}
.post{position:absolute;top:186px;width:292px;height:360px}
.post .photo{width:292px;height:196px;border-radius:6px 6px 0 0}
.post:nth-of-type(1){left:130px}
.post:nth-of-type(2){left:453px}
.post:nth-of-type(3){left:775px}
.photo.a{background:linear-gradient(160deg,#4d5a38,#2e3326 60%,#6b6a5a)}
.photo.b{background:linear-gradient(180deg,#7fa2c8 0%,#3f6a32 45%,#a7773b 100%)}
.photo.c{background:linear-gradient(180deg,#f2b45a 0%,#9fb7c4 45%,#4e6b83 100%)}
.post .card{position:absolute;left:16px;top:158px;width:260px;height:202px;background:var(--yellow);
  border-radius:6px;text-align:center;padding:16px 14px}
.card h3{font-weight:400;font-size:17px;line-height:26px}
.card time{display:block;margin:10px 0 8px;font-weight:500;font-size:16px}
.card p{font-size:12.5px;line-height:21px}

.map{position:absolute;left:0;top:1868px;width:1200px;height:472px;
  background:radial-gradient(ellipse at 52% 60%,var(--park) 0%,#dfe6d2 22%,var(--map) 48%)}

.footer{position:absolute;left:0;top:2340px;width:1200px;height:150px}
.social{position:absolute;left:541px;top:46px;display:flex;gap:6px}
.social span{width:25px;height:25px;border:2px solid var(--ink);border-radius:50%}
.footer p{position:absolute;top:92px;width:100%;text-align:center;font-size:13px}
</style>
</head>
<body>

<header class="hero" role="img" aria-label="Photo of the park at dusk with a pagoda tower, trees and lawn">
  <div class="hero-emblem">Harborline Hound Fair</div>
  <div class="ribbon name">
    <svg width="680" height="68" viewBox="0 0 680 68"><polygon points="0,0 680,0 655,34 680,68 0,68 25,34" fill="#fdc10e"/></svg>
    <span>Name - Harborline Hound Fair</span>
  </div>
  <div class="ribbon date">
    <svg width="680" height="68" viewBox="0 0 680 68"><polygon points="0,0 680,0 655,34 680,68 0,68 25,34" fill="#e4112b"/></svg>
    <span>Date / Time - May 11th, 2019 from 11am-6pm</span>
  </div>
  <div class="ribbon venue">
    <svg width="680" height="68" viewBox="0 0 680 68"><polygon points="0,0 680,0 655,34 680,68 0,68 25,34" fill="#fdc10e"/></svg>
    <span>Venue - Wexley Green, Baltimore MD</span>
  </div>
</header>

<section class="happenings">
  <svg class="edge" width="1200" height="80" viewBox="0 0 1200 80">
    <polygon points="0,0 600,72 1200,0 1200,-10 0,-10" fill="#26371e"/>
    <polyline points="0,0 600,72 1200,0" fill="none" stroke="#111" stroke-width="6"/>
  </svg>
  <h2>Some Of The Happenings In The Expo Are Below.</h2>
  <ul class="list left">
    <li><svg width="20" height="20" viewBox="0 0 20 20"><circle cx="10" cy="10" r="8.5" fill="none" stroke="#111" stroke-width="1.8"/><path d="M6 10h8M10.5 6.5 14 10l-3.5 3.5" fill="none" stroke="#111" stroke-width="1.8"/></svg>220 Exhibitors from NY to D.C.!</li>
    <li><svg width="20" height="20" viewBox="0 0 20 20"><circle cx="10" cy="10" r="8.5" fill="none" stroke="#111" stroke-width="1.8"/><path d="M6 10h8M10.5 6.5 14 10l-3.5 3.5" fill="none" stroke="#111" stroke-width="1.8"/></svg>Talks on BSL and Animal cruelty!</li>
    <li><svg width="20" height="20" viewBox="0 0 20 20"><circle cx="10" cy="10" r="8.5" fill="none" stroke="#111" stroke-width="1.8"/><path d="M6 10h8M10.5 6.5 14 10l-3.5 3.5" fill="none" stroke="#111" stroke-width="1.8"/></svg>Food Trucks!</li>
    <li><svg width="20" height="20" viewBox="0 0 20 20"><circle cx="10" cy="10" r="8.5" fill="none" stroke="#111" stroke-width="1.8"/><path d="M6 10h8M10.5 6.5 14 10l-3.5 3.5" fill="none" stroke="#111" stroke-width="1.8"/></svg>Live Music!</li>
  </ul>
  <div class="partner">
    <span class="dot"></span>
    <p>Kindness Knows No Breed</p>
  </div>
  <ul class="list right">
    <li><svg width="20" height="20" viewBox="0 0 20 20"><circle cx="10" cy="10" r="8.5" fill="none" stroke="#111" stroke-width="1.8"/><path d="M6 10h8M10.5 6.5 14 10l-3.5 3.5" fill="none" stroke="#111" stroke-width="1.8"/></svg>On-Site Adoptions with T.O.P.S.s, Renowned Pitbull advocates Velvet Paws Collective and Kindness Knows No Breed, Baltimore rescue Harbor Lantern Rescue!</li>
    <li><svg width="20" height="20" viewBox="0 0 20 20"><circle cx="10" cy="10" r="8.5" fill="none" stroke="#111" stroke-width="1.8"/><path d="M6 10h8M10.5 6.5 14 10l-3.5 3.5" fill="none" stroke="#111" stroke-width="1.8"/></svg>Games!</li>
    <li><svg width="20" height="20" viewBox="0 0 20 20"><circle cx="10" cy="10" r="8.5" fill="none" stroke="#111" stroke-width="1.8"/><path d="M6 10h8M10.5 6.5 14 10l-3.5 3.5" fill="none" stroke="#111" stroke-width="1.8"/></svg>Contest!</li>
    <li><svg width="20" height="20" viewBox="0 0 20 20"><circle cx="10" cy="10" r="8.5" fill="none" stroke="#111" stroke-width="1.8"/><path d="M6 10h8M10.5 6.5 14 10l-3.5 3.5" fill="none" stroke="#111" stroke-width="1.8"/></svg>Kids Corner!</li>
  </ul>
</section>

<section class="blog" role="region" aria-label="Latest blog, over a darkened photo of a bulldog">
  <h2>Latest Blog</h2>
  <article class="post">
    <div class="photo a" role="img" aria-label="Photo of a grey bully dog standing among trees"></div>
    <div class="card">
      <h3>Sed ut perspiciatis unde omnis iste natus</h3>
      <time>&#128197; Oct 01, 2018</time>
      <p>Quis autem vel eum iure reprehenderit qui in ea voluptate velit esse quam nihil mstiae consequatur</p>
    </div>
  </article>
  <article class="post">
    <div class="photo b" role="img" aria-label="Photo of a brown pitbull sitting in a sunny field"></div>
    <div class="card">
      <h3>Sed ut perspiciatis unde omnis iste natus</h3>
      <time>&#128197; Oct 01, 2018</time>
      <p>Quis autem vel eum iure reprehenderit qui in ea voluptate velit esse quam nihil mstiae consequatur</p>
    </div>
  </article>
  <article class="post">
    <div class="photo c" role="img" aria-label="Photo of a bulldog by a lake at sunset"></div>
    <div class="card">
      <h3>Sed ut perspiciatis unde omnis iste natus</h3>
      <time>&#128197; Oct 01, 2018</time>
      <p>Quis autem vel eum iure reprehenderit qui in ea voluptate velit esse quam nihil mstiae consequatur</p>
    </div>
  </article>
</section>

<div class="map" role="img" aria-label="Street map of Wexley Green, Baltimore, with the park outlined"></div>

<footer class="footer">
  <div class="social"><span></span><span></span><span></span><span></span></div>
  <p>© Copyright 2018 Dog Expo. All Rights Reserved.</p>
</footer>

</body>
</html>
```